Landscaping flier 2024

Create a 1 page flier for landscaping services
1. Must be completed in Adobe Photoshop
2. Size 8.5" x 11" (portrait layout)
3. Include logo
4. Text to include:
2024 Gravesite Landscaping Packages
info@maplecrestmemorial.example
(201) 555-0148
maplecrestmemorial.example
5. Use chart text for the content. DO NOT COPY THE CHART DESIGN/FORMAT. Use the chart for the text you need only.
6. Use "Pricing cards as format for laying out the chart". Open to other ideas as well.
**Use the example of chart design (handwritten) to base your design off of.
7. Photos
-include before and after care photos

```html
<!DOCTYPE html>
<html lang="en">
<head>
<meta charset="utf-8">
<title>2024 Gravesite Landscaping Packages</title>
<link href="https://fonts.googleapis.com/css2?family=Poppins:wght@300;400;500;600;700;800&display=swap" rel="stylesheet">
<style>
:root{
  --maroon:#7a1e2e;
  --maroon-deep:#5a1220;
  --maroon-dark:#3e0b14;
  --charcoal:#242122;
  --gold:#d6b21c;
  --card:#f1f1f1;
  --card-stripe:#e4e4e4;
  --card-head:#d8d8d8;
  --ink:#2b2b2b;
  --muted:#4a4a4a;
  --white:#ffffff;
  --stage:#ececec;
}
*{box-sizing:border-box;margin:0;padding:0}
html,body{width:1200px;height:2366px;overflow:hidden}
body{background:var(--stage);font-family:"Poppins",sans-serif;position:relative}
.flier{position:absolute;left:50px;top:471px;width:1100px;height:1424px;background:var(--white);overflow:hidden;box-shadow:0 6px 28px rgba(0,0,0,.18)}
.brand{position:absolute;top:92px;left:0;width:100%;display:flex;justify-content:center;align-items:center;gap:22px}
.brand-mark{width:58px;height:58px;border-radius:50%;background:var(--maroon)}
.brand-name{font-weight:500;font-size:46px;letter-spacing:3px;color:var(--maroon);white-space:nowrap}
.hero-band{position:absolute;left:0;top:228px;width:100%;height:416px;background:radial-gradient(ellipse at 12% 40%,#8e2a36 0%,transparent 45%),radial-gradient(ellipse at 88% 60%,#8a2533 0%,transparent 45%),linear-gradient(180deg,var(--maroon-deep),var(--maroon) 60%,var(--maroon-deep))}
.hero-dome{position:absolute;left:446px;top:186px;width:208px;height:84px;border-radius:104px 104px 0 0;background:var(--maroon-deep)}
.headline{position:absolute;top:246px;left:0;width:100%;text-align:center;color:var(--white);line-height:1}
.headline .year-line{display:block;font-weight:800;font-size:92px;letter-spacing:1px}
.headline .sub-line{display:block;font-weight:700;font-size:57px;margin-top:4px;letter-spacing:.5px}
.photo{position:absolute;top:416px;width:478px;height:307px;display:flex;flex-direction:column}
.photo-before{left:57px}
.photo-after{left:565px}
.photo-fill{flex:1;border:1px solid #fff}
.photo-before .photo-fill{background:linear-gradient(180deg,#8d9392 0%,#7f8a7c 22%,#5f8a3c 40%,#6fa844 70%,#5e9a39 100%)}
.photo-after .photo-fill{background:linear-gradient(180deg,#8f9594 0%,#7d867a 22%,#3f6a2c 45%,#6aa541 68%,#5c9838 100%)}
.photo-label{height:43px;background:var(--maroon);color:var(--white);font-weight:700;font-size:32px;display:flex;align-items:center;justify-content:center;letter-spacing:.5px}
.footer-band{position:absolute;left:0;top:1227px;width:100%;height:197px;background:var(--maroon)}
.valid{position:absolute;top:1306px;left:0;width:100%;text-align:center;color:var(--white);font-weight:800;font-size:24px;letter-spacing:-.5px}
.contacts{position:absolute;top:1348px;left:40px;right:40px;display:flex;justify-content:space-between;align-items:center;color:var(--white);font-size:18.5px;font-weight:400}
.contact{display:flex;align-items:center;gap:10px;white-space:nowrap}
.contact-icon{flex:none;width:34px;height:34px;border-radius:50%;border:2px solid var(--white);background:var(--charcoal);display:flex;align-items:center;justify-content:center}
.contact-icon svg{width:18px;height:18px}
.plans{position:absolute;top:786px;left:57px;width:986px;display:flex;gap:8px}
.plan{position:relative;width:323px;height:500px;background:var(--card);border-radius:12px;box-shadow:0 2px 6px rgba(0,0,0,.15)}
.plan-head{position:absolute;left:0;top:0;width:100%;height:122px;background:var(--card-head);border-radius:12px 12px 0 0;clip-path:polygon(0 0,100% 0,100% 52%,50% 82%,0 52%)}
.plan-tab{position:absolute;left:38px;top:-12px;width:247px;height:82px;color:var(--white);clip-path:polygon(0 0,100% 0,100% 74%,50% 100%,0 74%);display:flex;flex-direction:column;align-items:center;padding-top:12px;font-weight:600;font-size:16.5px;line-height:1.2;text-align:center}
.plan-seasonal .plan-tab,.plan-perpetual .plan-tab{background:var(--maroon)}
.plan-basic .plan-tab{background:var(--charcoal)}
.plan-seasonal .plan-tab{padding-top:20px}
.plan-perpetual .plan-tab{padding-top:6px}
.popular{margin-top:3px;width:247px;height:20px;background:var(--gold);font-size:12.5px;font-weight:400;line-height:20px;color:var(--charcoal)}
.plan-sub{position:absolute;top:86px;left:0;width:100%;text-align:center;font-weight:600;font-size:11.5px;line-height:1.3;color:var(--ink)}
.plan-body{position:absolute;top:140px;left:0;width:100%}
.feature{display:flex;align-items:flex-start;gap:8px;font-size:16.5px;font-weight:400;color:var(--ink);line-height:1.15}
.feature svg{flex:none;width:18px;height:18px;margin-top:2px}
.feature-lead{justify-content:center;text-align:center;padding:0 20px;height:62px}
.note{text-align:center;font-size:11.5px;color:var(--muted);line-height:1.25;padding:0 14px;height:52px}
.row{padding:0 34px;display:flex;align-items:center}
.row.tall{height:52px}
.row.short{height:42px}
.row.striped{background:var(--card-stripe)}
</style>
</head>
<body>
<div class="flier">
  <header class="brand">
    <span class="brand-mark"></span>
    <span class="brand-name">MAPLECREST MEMORIAL</span>
  </header>

  <div class="hero-dome"></div>
  <section class="hero-band" role="img" aria-label="Deep red autumn tree foliage backdrop"></section>
  <h1 class="headline"><span class="year-line">2024 GRAVESITE</span><span class="sub-line">LANDSCAPING PACKAGES</span></h1>

  <figure class="photo photo-before">
    <div class="photo-fill" role="img" aria-label="Gravesite before care: headstone with an overgrown, weedy plot on green lawn"></div>
    <figcaption class="photo-label">BEFORE</figcaption>
  </figure>
  <figure class="photo photo-after">
    <div class="photo-fill" role="img" aria-label="Gravesite after care: headstone with a neatly trimmed boxwood bed and flat marker"></div>
    <figcaption class="photo-label">AFTER</figcaption>
  </figure>

  <div class="footer-band"></div>

  <svg width="0" height="0" style="position:absolute">
    <defs>
      <symbol id="tick" viewBox="0 0 20 20"><circle cx="10" cy="10" r="10" fill="#3aa845"/><path d="M5.5 10.3l3 3 6-6.3" fill="none" stroke="#fff" stroke-width="2.2" stroke-linecap="round" stroke-linejoin="round"/></symbol>
      <symbol id="cross" viewBox="0 0 20 20"><circle cx="10" cy="10" r="10" fill="#e0313b"/><path d="M6.5 6.5l7 7M13.5 6.5l-7 7" stroke="#fff" stroke-width="2.2" stroke-linecap="round"/></symbol>
    </defs>
  </svg>

  <section class="plans">
    <article class="plan plan-seasonal">
      <div class="plan-head"></div>
      <div class="plan-tab">SEASONAL<br>CARE</div>
      <p class="plan-sub">SEASONAL<br>LANDSCAPING CARE</p>
      <div class="plan-body">
        <div class="feature feature-lead"><svg><use href="#tick"/></svg><span>Weeding &amp; trimming on<br>your gravesite</span></div>
        <p class="note">Approximately every 7 weeks during the growing season : mid-April through mid-October</p>
        <div class="feature row short striped"><svg><use href="#cross"/></svg><span>Monument leveling</span></div>
        <div class="feature row tall"><svg><use href="#cross"/></svg><span>Payment ensures grave<br>care forever</span></div>
        <div class="feature row short striped"><svg><use href="#cross"/></svg><span>Full bed of boxwood shrubs</span></div>
        <div class="feature row short"><svg><use href="#cross"/></svg><span>Replacement of shrubs</span></div>
        <div class="feature row short striped"><svg><use href="#cross"/></svg><span>Trust certificate</span></div>
      </div>
    </article>

    <article class="plan plan-basic">
      <div class="plan-head"></div>
      <div class="plan-tab">BASIC CARE<br>ENDOWMENT</div>
      <p class="plan-sub">LANDSCAPING CARE FOREVER<br>WITH NO PLASTING</p>
      <div class="plan-body">
        <div class="feature feature-lead"><svg><use href="#tick"/></svg><span>Weeding &amp; trimming on<br>your gravesite</span></div>
        <p class="note">2 times per year : mid-May &amp;<br>mid-September</p>
        <div class="feature row short striped"><svg><use href="#tick"/></svg><span>Monument leveling</span></div>
        <div class="feature row tall"><svg><use href="#tick"/></svg><span>Payment ensures grave<br>care forever</span></div>
        <div class="feature row short striped"><svg><use href="#cross"/></svg><span>Full bed of boxwood shrubs</span></div>
        <div class="feature row short"><svg><use href="#cross"/></svg><span>Replacement of shrubs</span></div>
        <div class="feature row short striped"><svg><use href="#cross"/></svg><span>Trust certificate</span></div>
      </div>
    </article>

    <article class="plan plan-perpetual">
      <div class="plan-head"></div>
      <div class="plan-tab">PERPETUAL CARE<br>ENDOWMENT<span class="popular">MOST POPULAR</span></div>
      <p class="plan-sub">LANDSCAPING CARE FOREVER<br>FOR GRAVES WITH PLASTRY</p>
      <div class="plan-body">
        <div class="feature feature-lead"><svg><use href="#tick"/></svg><span>Weeding &amp; trimming on<br>your gravesite</span></div>
        <p class="note">Approximately every 7 weeks during the growing season : mid-April through mid-October</p>
        <div class="feature row short striped"><svg><use href="#tick"/></svg><span>Monument leveling</span></div>
        <div class="feature row tall"><svg><use href="#tick"/></svg><span>Payment ensures grave<br>care forever</span></div>
        <div class="feature row short striped"><svg><use href="#tick"/></svg><span>Full bed of boxwood shrubs</span></div>
        <div class="feature row short"><svg><use href="#tick"/></svg><span>Replacement of shrubs</span></div>
        <div class="feature row short striped"><svg><use href="#tick"/></svg><span>Trust certificate</span></div>
      </div>
    </article>
  </section>

  <p class="valid">VALID THROUGH 10/31/2024</p>
  <footer class="contacts">
    <span class="contact"><span class="contact-icon"><svg viewBox="0 0 24 24"><path d="M6.6 10.8c1.4 2.8 3.8 5.1 6.6 6.6l2.2-2.2c.3-.3.7-.4 1-.2 1.1.4 2.3.6 3.6.6.6 0 1 .4 1 1V20c0 .6-.4 1-1 1C10.6 21 3 13.4 3 4c0-.6.4-1 1-1h3.5c.6 0 1 .4 1 1 0 1.3.2 2.5.6 3.6.1.3 0 .7-.2 1z" fill="#fff"/></svg></span>(201) 555-0148</span>
    <span class="contact"><span class="contact-icon"><svg viewBox="0 0 24 24"><rect x="3" y="5.5" width="18" height="13" rx="1.5" fill="#fff"/><path d="M3.5 6.5l8.5 6.5 8.5-6.5" fill="none" stroke="#242122" stroke-width="1.6"/></svg></span>info@maplecrestmemorial.example</span>
    <span class="contact"><span class="contact-icon"><svg viewBox="0 0 24 24" fill="none" stroke="#fff" stroke-width="1.6"><circle cx="12" cy="12" r="9"/><ellipse cx="12" cy="12" rx="4" ry="9"/><path d="M3 12h18M4.5 7.5h15M4.5 16.5h15"/></svg></span>www.maplecrestmemorial.example</span>
  </footer>
</div>
</body>
</html>
```